Drywall plastering business card design

Attached is my new logo and a picture of my current business card. I would like my new logo incorporated in to the business card and also my website which is:
www.kowhaibaywallcraftsolutions.co.nz
Industry/Entity Type
Business
Contact Information for Business Card
I would like a picture of my van and my new logo on my new business card. See attached files for pictures of my old business card, van picture and logo.
Colors
0555a3
ffffff
Requirements
Must have
- New logo, Van, contact info

```html
<!DOCTYPE html>
<html lang="en">
<head>
<meta charset="utf-8">
<title>Kowhai Bay Wallcraft Solutions – Business Card</title>
<link rel="stylesheet" href="https://fonts.googleapis.com/css2?family=Lato:wght@400;700;900&family=Courgette&display=swap">
<style>
  :root {
    --brand-blue: #0555a3;
    --brand-white: #ffffff;
    --ink: #1f1f1f;
    --stage: #2b2b2b;
    --sky-top: #3f86d6;
    --sky-low: #a9cdf0;
    --hill: #6f7f86;
    --road: #b3aa98;
    --road-dark: #8f8878;
  }
  * { box-sizing: border-box; margin: 0; padding: 0; }
  html, body {
    width: 1200px; height: 873px; overflow: hidden;
    background: var(--stage);
  }
  .business-card {
    position: absolute; left: 150px; top: 180px;
    width: 900px; height: 514px;
    background: var(--brand-white);
    overflow: hidden;
    font-family: "Lato", Arial, sans-serif;
    color: var(--ink);
    box-shadow: 0 18px 40px rgba(0,0,0,.55);
  }
  .van-photo {
    position: absolute; left: 250px; top: 0; right: 0; bottom: 0;
    background:
      linear-gradient(180deg, var(--sky-top) 0%, var(--sky-low) 38%, var(--hill) 52%, var(--road) 66%, var(--road-dark) 100%);
  }
  .van-photo::after {
    content: ""; position: absolute; inset: 0;
    background: linear-gradient(90deg, var(--brand-white) 0%, rgba(255,255,255,.85) 18%, rgba(255,255,255,0) 42%),
                linear-gradient(0deg, rgba(255,255,255,.7) 0%, rgba(255,255,255,0) 40%);
  }
  .brand-name {
    position: absolute; left: 70px; top: 120px;
    display: flex; align-items: center; gap: 14px;
    font-weight: 900; font-size: 30px; line-height: 1.05;
    color: var(--brand-blue);
    text-transform: uppercase;
  }
  .brand-mark {
    width: 46px; height: 46px; background: var(--brand-blue); flex: none;
  }
  .owner {
    position: absolute; left: 565px; top: 40px;
  }
  .owner-name { font-weight: 900; font-size: 30px; color: var(--brand-white); }
  .owner-role { font-weight: 700; font-size: 21px; color: var(--ink); margin-top: 2px; }
  .tagline {
    position: absolute; right: 40px; bottom: 110px;
    font-family: "Courgette", cursive;
    font-size: 30px; line-height: 1.15;
    color: var(--brand-blue);
  }
  .contact-tab {
    position: absolute; left: 0; bottom: 40px;
    width: 64px; height: 170px;
    background: var(--brand-blue);
    border-radius: 0 14px 14px 0;
    display: flex; flex-direction: column; justify-content: space-around; align-items: center;
    padding: 10px 0;
  }
  .contact-tab svg { width: 30px; height: 30px; fill: none; stroke: var(--brand-white); stroke-width: 2.4; stroke-linecap: round; stroke-linejoin: round; }
  .contact-list {
    position: absolute; left: 90px; bottom: 40px;
    height: 170px;
    list-style: none;
    display: flex; flex-direction: column; justify-content: space-around;
    font-weight: 700; font-size: 23px; letter-spacing: .2px;
  }
</style>
</head>
<body>
  <main class="business-card">
    <div class="van-photo" role="img" aria-label="Photo of the white company van parked on a gravel lookout with lake, mountains and blue sky behind"></div>

    <div class="brand-name">
      <span class="brand-mark"></span>
      <span>Kowhai Bay<br>Wallcraft Solutions</span>
    </div>

    <div class="owner">
      <p class="owner-name">Tane Hollis</p>
      <p class="owner-role">Proprietor</p>
    </div>

    <p class="tagline">Large jobs or small..<br>Always quality assured</p>

    <div class="contact-tab">
      <svg viewBox="0 0 24 24" aria-label="Phone"><path d="M5 4h4l2 5-2.5 1.5a11 11 0 0 0 5 5L15 13l5 2v4a2 2 0 0 1-2 2A16 16 0 0 1 3 6a2 2 0 0 1 2-2z"/></svg>
      <svg viewBox="0 0 24 24" aria-label="Email"><rect x="3" y="5" width="18" height="14" rx="1"/><path d="M3 6l9 7 9-7"/></svg>
      <svg viewBox="0 0 24 24" aria-label="Website"><path d="M10 14a4 4 0 0 0 5.6 0l3-3a4 4 0 0 0-5.6-5.6l-1.5 1.5"/><path d="M14 10a4 4 0 0 0-5.6 0l-3 3a4 4 0 0 0 5.6 5.6l1.5-1.5"/></svg>
    </div>

    <ul class="contact-list">
      <li>027 555 0142</li>
      <li>hello@kowhaibaywallcraft.co.nz</li>
      <li>www.kowhaibaywallcraftsolutions.co.nz</li>
    </ul>
  </main>
</body>
</html>
```